Tech Website

1. Overview
Lumora9, formally named VantaSight, is a pioneer in computer vision technology and machine learning. Based out of Santa Clara, California, Lumora9 is at the forefront of the User Interface revolution; building technology architecture that grants devices with the aptitude to respond to emotional detection, gaze tracking, facial recognition, age and gender identification and gaming interaction. Winner of the Mobile Track at BRISK Founders Sprint 2012, Lumora9 has developed the next generation of consumer behaviour analytics. Lumora9 software solutions are scalable across various platforms including mobile phone, tablets, PC and SmartTV.
Updates

Good day, 

Please see the update to our brief - there is a PDF of the type of format and design we are looking for.  It shows each page - Landing, Technology, Product, Press and Company.

Thank you for your designs

Regards,

Target Market(s)

Target market - A mix of enterprise and consumer audiences, targeting the need for the technology in the living room space

Industry/Entity Type

Architecture

Requirements
Must have
• Design preferences - Easy to navigate, modern with sleek feel, trendy, tech saavy, using cube as a consistent element/theme. colours are not determined, but parrot green was one idea with 2 additional underlying colours. keys words like user interface revolution or sense recognition are good sources to draw inspiration.

Landing page will have a video - illustrating different uses of technology

Technical Specs - Landing page, 6 tabs/subpages, and each subpage may have 1 or 2 additional pages. Coding will be necessary, not that much at the beginning stages.

```html
<!DOCTYPE html>
<html lang="en">
<head>
<meta charset="utf-8">
<title>Lumora9 — Home</title>
<link href="https://fonts.googleapis.com/css2?family=Ubuntu:wght@300;400;500&family=Cookie&display=swap" rel="stylesheet">
<style>
:root{
  --green-top:#5cb646;
  --green-mid:#3a9a2c;
  --green-deep:#1f7a1a;
  --page-bg:#eeeeee;
  --panel:#ffffff;
  --ink:#333333;
  --ink-soft:#555555;
  --logo-grey:#8a8a8a;
  --slider-bg:#d6d6d6;
  --icon-grey:#9a9a9a;
}
*{margin:0;padding:0;box-sizing:border-box}
html,body{width:1200px;height:990px;overflow:hidden}
body{position:relative;background:var(--page-bg);font-family:Arial,Helvetica,sans-serif;color:var(--ink)}
.abs{position:absolute}

.site-header{left:0;top:0;width:1200px;height:132px;background:linear-gradient(180deg,var(--green-top) 0%,var(--green-mid) 55%,var(--green-deep) 100%)}
.brand{left:150px;top:14px;display:flex;align-items:center;gap:10px}
.brand-mark{width:46px;height:46px;background:#f1f1f1;border-radius:4px}
.brand-name{font-family:'Ubuntu',sans-serif;font-weight:300;font-size:33px;color:#ffffff;letter-spacing:-.5px}
.search{left:844px;top:30px;width:197px;height:28px;background:#fff;border:1px solid #cfcfcf;border-radius:4px}
.search svg{position:absolute;right:8px;top:5px}

.main-nav a{position:absolute;top:103px;font-family:'Ubuntu',sans-serif;font-size:16px;color:#fff;text-decoration:none}
.main-nav .is-active{left:120px;top:97px;width:100px;height:36px;background:#fff;border-radius:10px 10px 0 0;color:var(--ink);text-align:center;padding-top:7px}

.content-panel{left:120px;top:132px;width:961px;height:342px;background:var(--panel);border-radius:0 12px 0 0}
.intro-title{left:140px;top:166px;font-family:'Cookie',cursive;font-weight:400;font-size:34px;color:#3a3a3a;border-bottom:2px solid #555;line-height:34px}
.intro-copy{left:140px;top:219px;width:280px;font-size:12px;letter-spacing:-.15px;line-height:17px;color:#444}
.intro-copy p+p{margin-top:17px}
.learn-more{left:139px;top:411px;width:94px;height:25px;background:linear-gradient(180deg,#63b84e,#2b8a22);clip-path:polygon(0 0,88% 0,100% 50%,88% 100%,0 100%);border-radius:4px 0 0 4px;color:#fff;font-size:10px;line-height:25px;padding-left:16px;letter-spacing:.3px}
.hero-video{left:436px;top:150px;width:626px;height:309px;border-radius:8px;background:radial-gradient(ellipse at 40% 80%,#e0a040 0%,#8a5a1c 35%,#3b2a12 65%,#1b1f30 100%)}
.play{position:absolute;background:#2a2a2a;border-radius:5px;display:flex;align-items:center;justify-content:center}
.hero-video .play{left:273px;top:127px;width:80px;height:56px;opacity:.92}

.lower-panel{left:120px;top:481px;width:961px;height:464px;background:var(--panel)}
.slider{left:128px;top:489px;width:943px;height:211px;background:var(--slider-bg)}
.slide{position:absolute;top:14px;width:286px;height:185px;border-radius:6px}
.slide .play{left:120px;top:83px;width:36px;height:25px;background:#111}
.s1{left:22px;background:linear-gradient(180deg,#2a3c5c,#4a6f8c 55%,#1e1e1e)}
.s2{left:328px;background:linear-gradient(180deg,#c9c9c9,#a9a9ad)}
.s3{left:634px;background:linear-gradient(180deg,#3f6d90,#2c8bb0 55%,#1a4a6a)}
.slider-arrow{position:absolute;top:96px}
.caption{top:709px;width:306px;text-align:center;font-family:'Ubuntu',sans-serif;font-size:15px;color:#444}

.featured-label{left:128px;top:749px;width:188px;height:57px;border:1px solid #bdbdbd;font-family:'Ubuntu',sans-serif;font-size:23px;color:#222;text-align:center;line-height:55px}
.featured-list{left:326px;top:749px;width:745px;height:57px;border:1px solid #bdbdbd;display:flex;align-items:center;justify-content:space-around;font-family:'Ubuntu',sans-serif;font-size:26px;font-weight:500;color:var(--logo-grey)}

.testimonial-title{left:138px;top:822px;font-family:'Cookie',cursive;font-weight:400;font-size:30px;color:#333}
.testimonial-copy{left:139px;top:853px;width:705px;font-size:12.3px;line-height:17px;color:#444}
.cta{left:872px;width:198px;height:46px;border-radius:4px;background:linear-gradient(180deg,#4bab3b,#1e7a18);color:#fff;font-family:'Ubuntu',sans-serif;font-size:14px;text-align:center;line-height:46px}

.site-footer{left:0;top:945px;width:1200px;height:45px;background:linear-gradient(180deg,var(--green-top),#4aa83a)}
.footer-nav{left:138px;top:953px;font-family:'Ubuntu',sans-serif;font-size:13px;color:#222}
.footer-nav span{margin:0 6px}
.copyright{left:138px;top:973px;font-size:10.5px;color:#2e5a22}
.social{left:867px;top:955px;display:flex;gap:6px}
.social i{width:24px;height:24px;border-radius:50%;background:var(--icon-grey);display:block}
</style>
</head>
<body>
<header class="abs site-header"></header>
<div class="abs brand"><span class="brand-mark"></span><span class="brand-name">LUMORA9</span></div>
<div class="abs search">
  <svg width="16" height="16" viewBox="0 0 16 16"><circle cx="6.5" cy="6.5" r="5" fill="none" stroke="#111" stroke-width="2.2"/><line x1="10" y1="10" x2="15" y2="15" stroke="#111" stroke-width="2.6" stroke-linecap="round"/></svg>
</div>
<nav class="main-nav">
  <a class="is-active" href="#">Home</a>
  <a href="#" style="left:259px">Technology</a>
  <a href="#" style="left:382px">Product</a>
  <a href="#" style="left:479px">Press</a>
  <a href="#" style="left:557px">Company</a>
</nav>

<section class="abs content-panel"></section>
<h1 class="abs intro-title">Lorem Ipsum:</h1>
<div class="abs intro-copy">
  <p>Lorem ipsum dolor sit amet, consectetuer adipiscing elit. Aenean commodo ligula eget dolor. Aenean massa. Cum sociis natoque penatibus et magnis dis parturient montes, nascetur ridiculus mus.Lorem ipsum dolor sit amet, consectetuer adipiscing elit. Aenean commodo ligula eget dolor.</p>
  <p>Aenean massa. Cum sociis natoque penatibus et magnis dis parturient montes, nascetur ridiculus mus.</p>
</div>
<a class="abs learn-more">LEARN MORE</a>
<div class="abs hero-video" role="img" aria-label="Video still looking up a tall circular atrium with golden floors">
  <div class="play"><svg width="30" height="34" viewBox="0 0 30 34"><polygon points="2,2 28,17 2,32" fill="#fff"/></svg></div>
</div>

<section class="abs lower-panel"></section>
<div class="abs slider">
  <svg class="slider-arrow" style="left:0" width="19" height="22" viewBox="0 0 19 22"><polygon points="19,0 8,11 19,22 11,22 0,11 11,0" fill="#2f8a28"/></svg>
  <div class="slide s1" role="img" aria-label="Tablet showing a home screen of apps"><div class="play"><svg width="14" height="14" viewBox="0 0 14 14"><polygon points="2,1 13,7 2,13" fill="#fff"/></svg></div></div>
  <div class="slide s2" role="img" aria-label="Two smartphones with a stylus"><div class="play"><svg width="14" height="14" viewBox="0 0 14 14"><polygon points="2,1 13,7 2,13" fill="#fff"/></svg></div></div>
  <div class="slide s3" role="img" aria-label="Smart TV showing an app menu"><div class="play"><svg width="14" height="14" viewBox="0 0 14 14"><polygon points="2,1 13,7 2,13" fill="#fff"/></svg></div></div>
  <svg class="slider-arrow" style="left:924px" width="19" height="22" viewBox="0 0 19 22"><polygon points="0,0 11,11 0,22 8,22 19,11 8,0" fill="#2f8a28"/></svg>
</div>
<div class="abs caption" style="left:140px">Tablet Pc</div>
<div class="abs caption" style="left:446px">Smart TV</div>
<div class="abs caption" style="left:752px">Mobile Phone</div>

<div class="abs featured-label">As Featured In</div>
<div class="abs featured-list">
  <span>Norvale</span><span>Quillo</span><span>Glintpost</span><span>Orvix</span><span>Kestrel Review</span>
</div>

<h2 class="abs testimonial-title">Testimonial</h2>
<p class="abs testimonial-copy">Lorem ipsum dolor sit amet, consectetuer adipiscing elit. Aenean commodo ligula eget dolor. Aenean massa. Cum sociis natoque penatibus et magnis dis parturient montes, nascetur ridiculus mus.Lorem ipsum dolor sit amet, consectetuer adipiscing elit. Aenean commodo ligula eget dolor. nascetur ridiculus mus.Lorem ipsum dolor sit amet, consectetuer adipiscing elit. Aenean commodo ligula eget dolor.</p>
<a class="abs cta" style="top:826px">Join Us At : VXE 2013 Jan 8-11</a>
<a class="abs cta" style="top:883px">Subcribe to LUMORA9 Blog</a>

<footer class="abs site-footer"></footer>
<div class="abs footer-nav">Home<span>|</span>Technology<span>|</span>Product<span>|</span>Press<span>|</span>Company<span>|</span>Contact Us</div>
<div class="abs copyright">Copyright © 2012 Lumora9. All rights reserved.</div>
<div class="abs social"><i></i><i></i><i></i><i></i><i></i><i></i><i></i></div>
</body>
</html>
```